Business card design needed

We require business cards for our young and innovative construction team.

Our business is Brask Constructions and we have used Lime, Navy and white with our colours so far.

We would like business cards that show our passion for perfection and detail, communication and management.

Looking forward to seeing the deigns!!

Contact Information for Business Card

Dan Pellow
Brask Constructions Pty Ltd
PO Box 782 Quarrow Flats NSW 2795
Mobile: 0471 392 608
Email: dpellow@braskconstructions.com.au
Web: www.braskconstructions.com.au

```html
<!DOCTYPE html>
<html lang="en">
<head>
<meta charset="utf-8">
<title>Brask Constructions – Business Card</title>
<link rel="stylesheet" href="https://fonts.googleapis.com/css2?family=Mulish:wght@400;700&display=swap">
<style>
  :root {
    --navy: #3d5079;
    --navy-deep: #34466d;
    --lime: #8cc63f;
    --paper: #f4f6f9;
    --backdrop: #e6e6ec;
    --ink: #3d5079;
  }
  * { margin: 0; padding: 0; box-sizing: border-box; }
  html, body {
    width: 1200px;
    height: 934px;
    overflow: hidden;
    background: var(--backdrop);
    font-family: "Mulish", sans-serif;
  }
  .sheet {
    position: relative;
    width: 1200px;
    height: 934px;
    display: flex;
    align-items: center;
    justify-content: center;
    gap: 60px;
  }
  .card {
    position: relative;
    width: 520px;
    height: 318px;
    overflow: hidden;
    box-shadow: 0 6px 18px rgba(40, 50, 80, 0.18);
  }
  .card--front {
    background: var(--navy);
    display: flex;
    align-items: center;
    justify-content: center;
  }
  .card--back {
    background: var(--paper);
  }
  .wordmark {
    display: flex;
    align-items: center;
    gap: 12px;
    font-weight: 700;
    font-size: 30px;
    letter-spacing: 0.5px;
    white-space: nowrap;
  }
  .wordmark__square {
    width: 18px;
    height: 18px;
    background: var(--lime);
  }
  .card--front .wordmark { color: #ffffff; }
  .card--back .wordmark {
    position: absolute;
    top: 72px;
    right: 34px;
    font-size: 26px;
    color: var(--ink);
  }
  .contact {
    position: absolute;
    left: 34px;
    top: 168px;
    color: var(--ink);
  }
  .contact__name {
    font-weight: 700;
    font-size: 15px;
    margin-bottom: 18px;
  }
  .contact__line {
    font-size: 10.5px;
    line-height: 16px;
    white-space: nowrap;
  }
  .contact__label {
    color: var(--lime);
    font-weight: 700;
  }
  .band {
    position: absolute;
    left: 0;
    right: 0;
    bottom: 0;
    height: 44px;
    background: var(--navy);
    border-top: 6px solid var(--lime);
  }
</style>
</head>
<body>
  <main class="sheet">
    <section class="card card--front" aria-label="Card front">
      <div class="wordmark"><span class="wordmark__square"></span>Brask Constructions</div>
    </section>

    <section class="card card--back" aria-label="Card back">
      <div class="wordmark"><span class="wordmark__square"></span>Brask Constructions</div>
      <div class="contact">
        <p class="contact__name">Dan Pellow</p>
        <p class="contact__line">PO Box 782 Quarrow Flats NSW 2795 · <span class="contact__label">M.</span> 0471 392 608</p>
        <p class="contact__line"><span class="contact__label">E.</span> dpellow@braskconstructions.com.au · <span class="contact__label">W.</span> www.braskconstructions.com.au</p>
      </div>
      <div class="band"></div>
    </section>
  </main>
</body>
</html>
```